Broschüren-Design für Wohnungsgesellschaft
Hallo Lukas, die Zusammenarbeit hat richtig Spaß gemacht. Ich empfanf die gedankliche Herangehensweise als sehr professionell, die vielen Varianten waren eine Hilfe mich am Ende doch für meine Bauchentscheidung für die ersten Designvorschläge zu bestätigen. Sie sind ein toller Dienstleister, schnelle Reaktionen, Mitdenken, dabei immer freundlich, auch wenn ich das 4 mal mit dem gleichen Thema kam.
Zielgruppe
wir betreuen im Auftrag der Wohnungsgesellschaften Mieter die ihre Miete oder Mietnebenkosten nicht oder nur teilweise bezahlen.
Ziel ist,in einer telefonischen, email, Whatsapp-Betreuung, den Schuldnern einen Ausweg zu zeigen.
Wir nehmen den Schulder quasi an die Hand um in gemeinsamer Abstimmung d,h, Augenhöhe
Teilzahlungspläne zu erarbeiten und jeweils auch einzuhalten.
Ziel ist es die Würde des Schuldners zu bewahren und der Wohnungsgesellschaft die ihr zustehenden Summen zu sichern.
Das Ganze sehr im Unterschied zu brutalen und teueren Inkasso Aktivitäten einschlägiger Firmen.
Aufgabenstellung
lebendige, freundliche Darstellung, ohne dümmliche Gesichter telfonierender Damen,
plaktiv, doch klar1. die Zielgruppe der Broschüre sind Vorstände und GF größerer Wohnungsgesellschaften.
Diese Menschen haben ein Problem, dass nicht bezahlte Mieten, den Unternehmensertrag und die Liquidität der Gesellschaft negativ beeinflussen.
2. Si3e wollen natürlich die Mieten kassieren, gleichzeitig wollen Sie sich nicht als brutale Geldeintreiber in der Tageszeitung und in den Köpfen aller anderen Mieter wahrgenommen werden.
3. bislang gibt es in jeder Gesellschaft angestellte Mitarbeiter, die meist untrainiert die Beitreibung betreiben. Der Job ist selten gerne übernommen, die Tagesform bestimmt den Ton. Wenn der Mitarbeiter ausfällt ist meist kein Ersatz da.
4. in der Regel startet kurz nach dem Fälligkeitstermin ein automatisiertes schriftliches Mahnverfahren (per Computer) mit 1-3 Stufen, danach wandert das ganze zu professionellen Inkassounternehmen, die dicke Mahngebühren berechnen, den Schuldner bedrohen bis hin zu persönlichen Besuchen, der Gerichtsvollzieher ist dann die noch moderate Form.
5. der BMQ Ansatz will genau das vermeiden, zumindest dort, wo ungeplante Umstände plötzliche Zahlungsengpässe verursachen oder Menschen nicht mit ihrem Geld richtig wirtschaften. Es geht nicht um die notorischen Zahlungsverweigerern.
Die Geschäftsführung der Gesellschaft soll und will das Gefühl haben, dass ihre Mieter auf Augenhöhe behandelt werden und genau deshalb kontinuierlich durch telefonische Ansprache, helfende Führung betreut werden, damit sie dartan arbeiten, die Mietshuld abzutragen und künftige Mieten pünktlich zahlen.
6. das wichtige Mittel ist der partnerschaftlich erstellte Zahlungsplan, der die Zahlungsmöglichkeiten in Raten des Mieters berücksichtig, der Grund ist, dass der Schuldner angesprochen werden kann, z.b. geht die Zahlung ein gelobt wird, kurz vorher an den Zahlungstermin erinn..

```html
<!DOCTYPE html>
<html lang="de">
<head>
<meta charset="utf-8">
<title>BMQ Immobilienservices – Broschüre</title>
<link href="https://fonts.googleapis.com/css2?family=Bitter:wght@400;500;700;800;900&display=swap" rel="stylesheet">
<style>
:root{
  --orange:#dc9129;
  --slate:#585856;
  --ink:#4a4a48;
  --paper:#ffffff;
  --rule:#8a8a88;
  --mist:#d8d8d4;
}
*{margin:0;padding:0;box-sizing:border-box}
html,body{width:1200px;height:2858px;overflow:hidden;background:var(--paper)}
body{position:relative;font-family:"Bitter",Georgia,serif;color:var(--ink)}
.page{position:absolute;width:360px;height:507px;border:1px solid var(--rule);overflow:hidden;background:var(--paper)}
.page--orange{background:var(--orange);color:#fff}
.page--slate{background:var(--slate);color:var(--mist)}
.abs{position:absolute}
.r{text-align:right}
.em{font-style:italic;font-weight:800}
.lead{font-size:15px;line-height:17px;font-weight:500}
.small{font-size:9.6px;line-height:11.6px}
.small p{margin-bottom:9px}
.headline{font-weight:900;color:var(--slate);font-size:31px;line-height:29px}
.footer-rule{position:absolute;left:26px;right:26px;top:481px;height:1px;background:currentColor;opacity:.8}
.footer-bar{position:absolute;top:479px;width:78px;height:3px}
.footer-text{position:absolute;top:486px;font-size:5px;font-weight:700;letter-spacing:.3px}
.brand{display:flex;align-items:center;gap:6px;font-size:19px;color:var(--slate)}
.brand__mark{width:12px;height:12px;background:var(--orange)}
.vertical{position:absolute;font-weight:900;writing-mode:vertical-rl;letter-spacing:1px}
.checks{list-style:none}
.checks li{display:flex;gap:9px;font-size:9.6px;line-height:11px;color:#8a8a86;margin-bottom:9px}
.checks svg{flex:none;margin-top:-1px}
</style>
</head>
<body>

<!-- Cover -->
<section class="page page--orange" style="left:598px;top:56px">
  <div class="abs" style="left:26px;top:26px;width:308px;height:455px;background:var(--paper)"></div>
  <div class="abs brand" style="left:70px;top:130px"><span class="brand__mark"></span>BMQ Immobilienservices</div>
  <div class="abs" style="left:43px;top:214px;width:273px;height:250px;background:var(--orange)"></div>
  <div class="abs lead" style="left:83px;top:254px;width:193px">
    <p>Mieter wollen ihre Miete pünktlich zahlen</p>
    <p class="em" style="font-size:18px;margin:10px 0 8px">Stimmt!</p>
    <p class="r">Manchmal kommt es leider anders.</p>
    <p class="r" style="margin-top:12px">Deshalb braucht es ein Optimiertes Mietschuldenmanagement.</p>
  </div>
</section>

<!-- Spread 1 left -->
<section class="page page--orange" style="left:239px;top:614px">
  <div class="abs lead r" style="left:14px;top:40px;width:158px">
    <p>Manche brauchen eine führende Hand</p>
    <p class="em" style="font-size:18px;margin:10px 0 9px">Stimmt!</p>
    <p>Sonst hilft nur noch Inkasso, damit Sie Ihr Geld bekommen</p>
    <p class="em" style="font-size:18px;margin:10px 0 9px">Stimmt nicht!</p>
    <p>Angst verursacht Flucht oder den Kopf in den Sand stecken.</p>
    <p style="margin-top:13px">Mietschulden­management 2.0 holt Ihr Geld auf Augenhöhe mit dem Schuldner.</p>
  </div>
  <div class="abs lead" style="left:187px;top:83px;width:150px;font-weight:400">
    <p>Unverhofft kommt oft. Nicht immer, doch meistens dann mitvoller Wucht.</p>
    <p style="margin-top:12px">Routinen werden Makulatur. Guter Wille allein genügt nicht mehr, wenn nur noch konkrete Hilfe dafür sorgt, dass der Kopf oben bleibt.</p>
    <p style="margin-top:12px">Ein empathischer Gesprächspartner öffnet den Blick auf das Machbare, zeigt Wege auf, erschließt Zahlungs­versprechen und die Bereitschaft diese auch einzuhalten.</p>
  </div>
  <div class="footer-rule"></div>
  <div class="footer-text" style="left:26px">2 | WWW.BMQ-IMMOBILIENSERVICES.DE</div>
</section>

<!-- Spread 1 right -->
<section class="page" style="left:598px;top:614px">
  <h2 class="abs headline" style="left:24px;top:37px">„Der frühe Vogel<br>pickt den Wurm.“</h2>
  <div class="abs small" style="left:26px;top:145px;width:150px;color:var(--orange)">
    <p>Es ist eine Binsenweisheit, dass Schuldner bei Geldeingang denjenigen Gläubiger zuerst befriedigen / ihre Verpflichtungen in Teilen abtragen, der zeitnah und emotional am nächsten ist.</p>
    <p>Deshalb erlebt Ihr Mieter mit M 2.0 keine Massenabfertigung!</p>
    <p>Er erhält seinen persönlichen Berater, der mit ihm im engeren Kontakt bleibt: sich für jede Zahlung per E-Mail oder SMS</p>
  </div>
  <div class="abs small" style="left:183px;top:145px;width:150px;color:var(--orange)">
    <p>bedankt, den nächsten Termin avisiert und den reduzierten Kontostand aufzeigt. Die Mietschulden bekommen eine achtsame, verständnisvolle Stimme, die nicht verurteilt sondern einen klaren Weg aus der nicht ganz einfachen Situation aufzeigt &amp; Mut macht.</p>
  </div>
  <p class="abs lead r" style="left:40px;top:357px;width:294px;color:var(--ink)">Ein noch so kleiner Schritt Richtung Kontoausgleich spornt an, verschafft Lob und Anerkennung ..., in der Lebenssituation als Schuldner ein überraschend unerwartetes und somit erleichterndes, positives Ereignis.</p>
  <div class="footer-rule" style="color:var(--rule)"></div>
  <div class="footer-bar" style="right:26px;background:var(--slate)"></div>
  <div class="footer-text r" style="right:26px;color:var(--ink)">WWW.BMQ-IMMOBILIENSERVICES.DE | 3</div>
</section>

<!-- Spread 2 left -->
<section class="page page--slate" style="left:239px;top:1171px">
  <h2 class="abs headline" style="left:26px;top:36px;color:var(--orange)">Samthand-<br>schuhe sind was<br>für Weicheier.</h2>
  <div class="abs small" style="left:26px;top:143px;width:150px">
    <p>Bei allem Verständnis für momentane oder strukturelle Engpässe, geht es mit M2.0 stets darum, dass Sie die Vertragsmiete oder die von Ihnen verauslagten Mietnebenkosten bezahlt bekommen.</p>
    <p>Nicht das ob, sondern das wie entscheidet ob Sie zulassen, dass hohe Inkassokosten den Mieter weiter in die Schuldenfalle treiben, Sie sich dabei wohlfühlen wie man mit Ihren Mietern umgeht.</p>
  </div>
  <p class="abs r" style="left:150px;top:250px;width:184px;color:var(--orange);font-weight:900;font-size:18.5px;line-height:20px">Deshalb muss ein konkreter Plan her der den Mieter atmen lässt, damit er zahlen kann.</p>
  <p class="abs small r" style="left:150px;top:400px;width:184px">Ein Plan, der den Möglichkeiten des Mieters Rechnung trägt und gleichzeitig Ihre Forderung in einem vertretbaren Zeitfenster bedient.</p>
  <div class="footer-rule"></div>
  <div class="footer-bar" style="left:26px;background:var(--mist)"></div>
  <div class="footer-text" style="left:26px">4 | WWW.BMQ-IMMOBILIENSERVICES.DE</div>
</section>

<!-- Spread 2 right -->
<section class="page" style="left:598px;top:1171px">
  <div class="vertical" style="left:24px;top:36px;font-size:56px;line-height:50px;color:#8a8a88">WER?</div>
  <div class="abs small" style="left:92px;top:123px;width:82px;color:var(--orange)">
    <p>Jemanden anzurufen, um mit ihm über seine Mietschulden zu sprechen, ist für die meisten Menschen kein erstrebenswerter Gedanke.</p>
  </div>
  <div class="abs small" style="left:26px;top:245px;width:150px;color:var(--orange)">
    <p>In einem Telefonat spüren die Gesprächspartner sehr schnell in welcher persönlichen Haltung, Stimmung der Gegenüber sich gerade befindet.</p>
    <p>Mietschulden-Manager (M2.0) der BMQ sind besondere Menschen mit dem nötigen Feingefühl, die in diversen Auswahlverfahren ihre Hilfsbereitschaft, ihre Empathie und gleichzeitig ihre Zielorientierung bewiesen haben.</p>
  </div>
  <div class="abs small" style="left:183px;top:123px;width:152px;color:var(--orange)">
    <p>Die Damen und Herren sind über die Fähigkeiten erfolgreicher Telefonagenten im Outbound hinaus, im Umgang mit Schuldnern und beim Verabreden von Zahlungsplänen geschult. Regelmäßiges site by site Coaching hält das Leistungsniveau hoch.</p>
    <p style="margin-top:12px">Es gilt eine Gesprächs­atmosphäre zu schaffen, in der es dem Schuldner leicht fällt über seine Sorgen und Nöte, somit auch über seine finanziellen Möglichkeiten offen zu sprechen, zu seinem Gesprächspartner Vertrauen aufzubauen.</p>
    <p>M2.0 Mitarbeiter sind „Mittelstrecken-Läufer“ Das Endergebnis zählt!</p>
    <p>Deshalb arbeiten unsere Mitarbeiter für ein fixes Monatsgehalt, erhalten für jeden erfolgreich zu Ende geführten Zahlungsplan ein Incentive.</p>
  </div>
  <div class="footer-rule" style="color:var(--rule)"></div>
  <div class="footer-bar" style="right:26px;background:var(--slate)"></div>
  <div class="footer-text r" style="right:26px;color:var(--ink)">WWW.BMQ-IMMOBILIENSERVICES.DE | 5</div>
</section>

<!-- Spread 3 left -->
<section class="page page--orange" style="left:239px;top:1728px">
  <div class="vertical" style="left:22px;top:40px;font-size:56px;line-height:50px;color:#fff">WIE?</div>
  <div class="abs small" style="left:82px;top:62px;width:94px">
    <p style="font-weight:800">Zusammenarbeit mit Ihnen</p>
    <p>Die M 2.0 Spezialisten der BMQ agieren als verlängerte Werkbank Ihres Hauses, in Ihrem Namen, mit Ihrer DNA.</p>
  </div>
  <div class="abs small" style="left:26px;top:198px;width:150px">
    <p>Sie werden durch eine Datensichere Point-to-Point Verbindung mit Ihrem System verbunden und können so im Echtzeitabgleich alle daraus sich ergebenen Schritte, im Mieterkonto und in der Kommunikation anstoßen.</p>
    <p>Alles bleibt in Ihrem System, das ist sicher und spart viel IT-Geld. M2.0 Spezialisten können Sie pro Person zu fixen Monatspauschalen, Tages / Stundensätzen / einkaufen.</p>
    <p>Für spezielle Sprachkenntnisse, für Aktivitäten außerhalb üblicher Geschäftszeiten, soweit gesetzliche Bestimmungen dies zulassen, legen wir gerne gesonderte Angebote vor.</p>
  </div>
  <div class="abs small" style="left:184px;top:62px;width:152px">
    <p style="font-weight:800">Zusammenarbeit mit den Mietschuldnern</p>
    <p>Sie legen fest ab welchem Zeitpunkt wir in Ihrem Namen aktiv werden: Ab welcher Mahnstufe, innerhalb welchem Zeitfenster, in welcher Frequenz, etc.</p>
    <p>Sobald wir zusammen mit Ihrem Mieter den konkreten Zahlungsplan festgelegt haben, wird er dem Mieter schriftlich bestätigt und von da an folgen per e-mail oder sms Erinnerungen an den nächsten Zahlungstermin, Dankeschön für Zahlungseingänge, aktueller Restschuldenstand oder auch erneute Anrufe in den Fällen mit besonderem Pflegebedarf.</p>
    <p>Ein effektives System mit persönlichen Mehrfach-Kontakt, als Motivation und Dauerpräsenz! Ihre Geldforderung zieht am Frustrstapel der Gläubigerpost vorbei, erfährt Emotionalität und wird zur Priorität Ihres Mieters.</p>
  </div>
  <div class="footer-rule"></div>
  <div class="footer-bar" style="left:26px;background:var(--slate)"></div>
  <div class="footer-text" style="left:26px">6 | WWW.BMQ-IMMOBILIENSERVICES.DE</div>
</section>

<!-- Spread 3 right -->
<section class="page" style="left:598px;top:1728px">
  <h2 class="abs headline" style="left:24px;top:32px">GEWINN für Ihr<br>Unternehmen</h2>
  <ul class="abs checks" style="left:26px;top:119px;width:160px">
    <li><svg width="14" height="14" viewBox="0 0 14 14"><circle cx="7" cy="7" r="7" fill="var(--orange)"/><path d="M3.5 7.2l2.4 2.4 4.6-5" fill="none" stroke="#fff" stroke-width="1.8"/></svg>Geringerer Mietenausfall</li>
    <li><svg width="14" height="14" viewBox="0 0 14 14"><circle cx="7" cy="7" r="7" fill="var(--orange)"/><path d="M3.5 7.2l2.4 2.4 4.6-5" fill="none" stroke="#fff" stroke-width="1.8"/></svg>Pfleglicherer Umgang<br>mit der Wohnung</li>
    <li><svg width="14" height="14" viewBox="0 0 14 14"><circle cx="7" cy="7" r="7" fill="var(--orange)"/><path d="M3.5 7.2l2.4 2.4 4.6-5" fill="none" stroke="#fff" stroke-width="1.8"/></svg>Geringere Mieterfluktuation</li>
    <li><svg width="14" height="14" viewBox="0 0 14 14"><circle cx="7" cy="7" r="7" fill="var(--orange)"/><path d="M3.5 7.2l2.4 2.4 4.6-5" fill="none" stroke="#fff" stroke-width="1.8"/></svg>Beständigere Hausgemeinschaft</li>
    <li><svg width="14" height="14" viewBox="0 0 14 14"><circle cx="7" cy="7" r="7" fill="var(--orange)"/><path d="M3.5 7.2l2.4 2.4 4.6-5" fill="none" stroke="#fff" stroke-width="1.8"/></svg>Ihre Immobilie behält sich den Wert weiterhin eine „Immobilie mit gutem Ruf“ zu sein, wo man gerne wohnt</li>
    <li><svg width="14" height="14" viewBox="0 0 14 14"><circle cx="7" cy="7" r="7" fill="var(--orange)"/><path d="M3.5 7.2l2.4 2.4 4.6-5" fill="none" stroke="#fff" stroke-width="1.8"/></svg>Imagegewinn als fürsorglicher Vermieter</li>
    <li><svg width="14" height="14" viewBox="0 0 14 14"><circle cx="7" cy="7" r="7" fill="var(--orange)"/><path d="M3.5 7.2l2.4 2.4 4.6-5" fill="none" stroke="#fff" stroke-width="1.8"/></svg>Termingerechte Aktivitäten, unabhängig von Urlaub, Krankheit, Mitarbeiterfluktuation</li>
    <li><svg width="14" height="14" viewBox="0 0 14 14"><circle cx="7" cy="7" r="7" fill="var(--orange)"/><path d="M3.5 7.2l2.4 2.4 4.6-5" fill="none" stroke="#fff" stroke-width="1.8"/></svg>Keine hohen Inkassokosten für Ihre Mieter</li>
    <li><svg width="14" height="14" viewBox="0 0 14 14"><circle cx="7" cy="7" r="7" fill="var(--orange)"/><path d="M3.5 7.2l2.4 2.4 4.6-5" fill="none" stroke="#fff" stroke-width="1.8"/></svg>Refinanzierungsmöglichkeit durch</li>
    <li><svg width="14" height="14" viewBox="0 0 14 14"><circle cx="7" cy="7" r="7" fill="var(--orange)"/><path d="M3.5 7.2l2.4 2.4 4.6-5" fill="none" stroke="#fff" stroke-width="1.8"/></svg>Geringe Gebühr für den Zahlungsplan an den Mieter</li>
  </ul>
  <div class="abs lead r" style="left:190px;top:174px;width:144px;color:var(--orange);font-weight:400">
    <p>Typisch<br>Call Center?</p>
    <p class="em" style="font-size:18px;margin:10px 0 8px">Nicht doch!</p>
    <p>Die BMQ ist ein seit mehr als 20 Jahren auf die Mieter­kommunikation großer und mittlerer Wohnungs­gesellschaften spezialisierter Dienstleister.</p>
    <p class="em" style="font-size:18px;margin-top:12px">Ja doch !</p>
  </div>
  <div class="footer-rule" style="color:var(--rule)"></div>
  <div class="footer-bar" style="right:26px;background:var(--slate)"></div>
  <div class="footer-text r" style="right:26px;color:var(--ink)">WWW.BMQ-IMMOBILIENSERVICES.DE | 7</div>
</section>

<!-- Back cover -->
<section class="page" style="left:239px;top:2285px">
  <div class="abs small" style="left:26px;top:38px;width:310px;font-size:10px;line-height:12px">
    <p>BMQ Immobilienservices versteht die Bedürfnisse ihrer Kunden in der Immobilienwirtschaft. Jährlich mehr als 600.000 Gespräche mit großer Sofortlösungs-Ambition sind eine solide Erfahrung. Es gibt nichts, was im Leben eines Mieters vorkommen kann, was unsere Mitarbeiter noch nicht erfahren hätten.</p>
    <p style="margin-top:12px">Fast 200 Mitarbeiter behandeln Havarie-Meldungen, Hinweise auf Mängel in der Verkehrssicherheit oder einfache Anliegen, falls im Winter morgens um 7 Uhr noch nicht geräumt sein sollte, der Hausmeister angeblich nicht funktioniert oder das Fenster kaputt gegangen ist.</p>
  </div>
  <p class="abs r" style="left:26px;top:192px;width:308px;color:var(--orange);font-weight:800;font-size:14px;line-height:16px">Immer Erreichbar 24/7/365. Zu jeder Stunde, jeden Tag, im ganzen Jahr. Das auch noch in Zertifizierter Qualität.</p>
  <div class="abs" style="left:26px;top:275px;width:150px;font-size:7px;line-height:9px">
    <p style="margin-bottom:7px">BMQ Immobilienservices ist nach DIN EN ISO 9001 sowie ISO/IEC 27001 zertifiziert.</p>
    <p style="margin-bottom:7px">Das bedeutet: Qualität und der Schutz sensibler Kundendaten sind gewährleistet.</p>
    <p style="margin-bottom:7px">Interne Kontrollen sorgen für weitere Sicherheit.</p>
    <p>Hier erfahren Sie mehr über unsere ISO Zertifizierungen.</p>
  </div>
  <svg class="abs" style="left:26px;top:392px" width="150" height="66" viewBox="0 0 150 66" role="img" aria-label="Zertifikatssiegel">
    <circle cx="31" cy="33" r="30" fill="none" stroke="var(--ink)" stroke-width="2"/>
    <circle cx="31" cy="33" r="22" fill="none" stroke="var(--ink)" stroke-width="1"/>
    <circle cx="111" cy="33" r="30" fill="none" stroke="var(--ink)" stroke-width="2"/>
    <circle cx="111" cy="33" r="22" fill="none" stroke="var(--ink)" stroke-width="1"/>
  </svg>
  <div class="abs brand" style="left:198px;top:290px;font-size:11px;gap:4px"><span class="brand__mark" style="width:8px;height:8px"></span>BMQ Immobilienservices</div>
  <p class="abs" style="left:198px;top:336px;font-size:7px;font-weight:700;color:var(--orange)">www.bmq-immobilienservices.de</p>
  <div class="abs" style="left:198px;top:364px;width:150px;font-size:6.5px;line-height:8px">
    <p style="font-weight:700">Hauptsitz Potsdam</p>
    <p>Lindenallee 42<br>14469 Potsdam<br>Telefon: +49 331/5550170<br>E-Mail: info@bmq-immobilienservices.de</p>
    <p style="font-weight:700;margin-top:6px">Niederlassung Brandenburg</p>
    <p>BMQ Immobilienservices<br>Uferweg 12<br>14770 Brandenburg an der Havel</p>
  </div>
</section>

</body>
</html>
```